New Business Card Design Project

New business card design required for an electrical business in Australia. Offering quality electrical services including design and installation. Electrical services offered are domestic, commercial and industrial. Also meets all the air conditioning installation and maintenance needs.

Target Market(s)

The business is sleek, professional and caters primarily to wealthy clients and government contracts looking for exceptional, tailored service.

Industry/Entity Type

Electrical

Contact Information for Business Card

Damian Corlowe (Director)
0438 615 274
admin@vrtelectrical.com.au
www.vrtelectrical.com.au

Font styles to use
Sans Serif

Requirements
Must have
• The business card must show the license number - 64193 to comply with legislation.
Nice to have
• The logo colours and fonts could be incorporated into the design if the designer sees fit. We are open to new ideas and welcome creativity. The logo style guide is attached for reference if required.

```html
<!DOCTYPE html>
<html lang="en">
<head>
<meta charset="utf-8">
<title>VRT Electrical — Business Card</title>
<link href="https://fonts.googleapis.com/css2?family=Montserrat:wght@400;500;700&display=swap" rel="stylesheet">
<style>
  :root {
    --backdrop: #93969b;
    --navy: #142a52;
    --paper: #e4e4e4;
    --ink: #3d3d3d;
    --white: #ffffff;
  }
  * { margin: 0; padding: 0; box-sizing: border-box; }
  html, body { width: 1200px; height: 900px; overflow: hidden; }
  body {
    background: var(--backdrop);
    font-family: "Montserrat", sans-serif;
    position: relative;
  }
  .card {
    position: absolute;
    left: 379px;
    width: 443px;
    height: 271px;
    border-radius: 21px;
    overflow: hidden;
  }
  .card--front { top: 145px; background: var(--navy); }
  .card--back { top: 484px; background: var(--paper); }

  .wordmark {
    position: absolute;
    font-weight: 500;
    white-space: nowrap;
    line-height: 1;
    letter-spacing: 0.02em;
  }
  .card--front .wordmark {
    right: 30px;
    top: 183px;
    font-size: 36px;
    color: var(--white);
  }
  .card--back .wordmark {
    left: 25px;
    top: 34px;
    font-size: 32px;
    color: var(--navy);
  }

  .holder {
    position: absolute;
    left: 25px;
    top: 147px;
  }
  .holder__name {
    font-weight: 700;
    font-size: 12px;
    letter-spacing: 0.04em;
    color: var(--navy);
    text-transform: uppercase;
  }
  .holder__role {
    font-size: 10.5px;
    color: var(--ink);
    margin-top: 1px;
  }

  .contacts {
    position: absolute;
    left: 25px;
    top: 196px;
    list-style: none;
  }
  .contacts__item {
    display: flex;
    align-items: center;
    gap: 7px;
    height: 14px;
    font-size: 10.5px;
    color: var(--ink);
    white-space: nowrap;
  }
  .contacts__icon { width: 9px; height: 9px; flex: none; }
</style>
</head>
<body>

  <section class="card card--front" aria-label="Card front">
    <div class="wordmark">VRT Electrical</div>
  </section>

  <section class="card card--back" aria-label="Card back">
    <div class="wordmark">VRT Electrical</div>

    <div class="holder">
      <p class="holder__name">Damian Corlowe</p>
      <p class="holder__role">Director</p>
    </div>

    <ul class="contacts">
      <li class="contacts__item">
        <svg class="contacts__icon" viewBox="0 0 10 10" aria-hidden="true">
          <path d="M2 0.8 L3.6 0.5 L4.3 2.8 L3.3 3.6 Q4.2 5.6 6.3 6.7 L7.1 5.7 L9.4 6.4 L9.1 8.1 Q8.6 9.4 7 9.2 Q1.5 7.8 0.7 2.6 Q0.7 1.2 2 0.8 Z" fill="var(--navy)"/>
        </svg>
        <span>0438 615 274</span>
      </li>
      <li class="contacts__item">
        <svg class="contacts__icon" viewBox="0 0 10 10" aria-hidden="true">
          <rect x="0.5" y="2" width="9" height="6.4" fill="var(--navy)"/>
          <path d="M0.8 2.3 L5 5.6 L9.2 2.3" fill="none" stroke="var(--paper)" stroke-width="0.8"/>
        </svg>
        <span>admin@vrtelectrical.com.au</span>
      </li>
      <li class="contacts__item">
        <svg class="contacts__icon" viewBox="0 0 10 10" aria-hidden="true">
          <circle cx="5" cy="5" r="4.5" fill="var(--navy)"/>
          <g fill="none" stroke="var(--paper)" stroke-width="0.6">
            <ellipse cx="5" cy="5" rx="1.8" ry="4.5"/>
            <line x1="0.5" y1="5" x2="9.5" y2="5"/>
            <line x1="1.2" y1="2.8" x2="8.8" y2="2.8"/>
            <line x1="1.2" y1="7.2" x2="8.8" y2="7.2"/>
          </g>
        </svg>
        <span>www.vrtelectrical.com.au</span>
      </li>
      <li class="contacts__item">
        <svg class="contacts__icon" viewBox="0 0 10 10" aria-hidden="true">
          <circle cx="5" cy="5" r="4.5" fill="var(--navy)"/>
          <path d="M2.8 5.1 L4.4 6.7 L7.3 3.5" fill="none" stroke="var(--paper)" stroke-width="1"/>
        </svg>
        <span>Lic. No. 64193</span>
      </li>
    </ul>
  </section>

</body>
</html>
```